Logo and Business Card Design for Innovative Corporate Law Firm

Variel Advogados is a new, young and innovative law firm focused in corporate law, mainly helping start-ups in the incorporation process, liasing with strategic investors, funds, private equity and venture/seed capital businesses around the world.

We need a logo and business card design that correctly captures our modern and savvy, yet sober, approach to legal practice.

We are looking to starting with the logo and business card designs and further ahead move on to stationery, website etc.

We are located in São Paulo/Brazil, but we expect our logo and stationery design to be able to reach and connect to possible clients worldwide due to the international characteristic of our practice.

Be creative! We have no restrictions on colors, one-sided or two-sided cards, logos, font styles...
Updates

Guys, just to be clear: The project shall contemplate a full stationery design, but the logo and business card may be proposed in advance due to our urgent need to have these cards ready for our clients. The other stationery items may be proposed later on. Many thanks!

Dear all, please be aware that the logo should look good both in collor and black and white. 

Thanks

Industry/Entity Type

Business

Requirements
Must have
• Modern but sober approach
Nice to have
• I tend to like grey collor schemes with red touches, but this is not a must have...
Should not have
• Excessively bright, shiny look, that will make our legal services look too commercial. No excesses.

```html
<!DOCTYPE html>
<html lang="pt-BR">
<head>
<meta charset="utf-8">
<title>Variel Advogados — Cartão de visita</title>
<link href="https://fonts.googleapis.com/css2?family=PT+Serif:wght@400;700&display=swap" rel="stylesheet">
<style>
  :root {
    --brand-red: #a3111c;
    --brand-grey: #8e9194;
    --text-grey: #6b6e71;
    --rule-grey: #b9bbbd;
    --card-white: #f4f4f3;
    --backdrop: #7c8e92;
  }
  * { margin: 0; padding: 0; box-sizing: border-box; }
  html, body {
    width: 1200px;
    height: 720px;
    overflow: hidden;
  }
  body {
    background: var(--backdrop);
    font-family: "PT Serif", Georgia, serif;
    position: relative;
  }
  .card {
    position: absolute;
    top: 200px;
    width: 540px;
    height: 310px;
    background: var(--card-white);
    box-shadow: 0 6px 18px rgba(0, 0, 0, 0.25);
  }
  .card--front { left: 40px; }
  .card--contact { left: 620px; }

  /* Front */
  .front-brand {
    position: absolute;
    left: 0;
    right: 0;
    top: 108px;
    display: flex;
    align-items: center;
    justify-content: center;
    gap: 14px;
  }
  .brand-dot {
    width: 22px;
    height: 22px;
    border-radius: 50%;
    background: var(--brand-grey);
  }
  .brand-name {
    color: var(--brand-red);
    font-weight: 700;
    font-size: 38px;
    letter-spacing: 1px;
  }
  .front-web {
    position: absolute;
    left: 0;
    right: 0;
    top: 200px;
    text-align: center;
    color: var(--brand-red);
    font-size: 17px;
  }

  /* Contact side */
  .contact-brand {
    position: absolute;
    left: 0;
    top: 0;
    width: 190px;
    height: 100%;
    display: flex;
    align-items: center;
    justify-content: center;
    gap: 10px;
  }
  .contact-brand .brand-dot { width: 16px; height: 16px; }
  .contact-brand .brand-name { font-size: 28px; letter-spacing: 0.5px; }
  .divider {
    position: absolute;
    left: 190px;
    top: 60px;
    width: 1px;
    height: 190px;
    background: var(--rule-grey);
  }
  .contact-details {
    position: absolute;
    left: 222px;
    top: 62px;
    right: 20px;
    color: var(--text-grey);
    font-size: 15px;
    line-height: 1.3;
  }
  .person-name {
    color: var(--brand-red);
    font-weight: 700;
    font-size: 21px;
    margin-bottom: 16px;
  }
  .address { margin-bottom: 6px; }
  .contact-line {
    display: flex;
    align-items: center;
    gap: 7px;
  }
  .contact-icon {
    width: 13px;
    height: 13px;
    flex: none;
    fill: var(--brand-red);
  }
</style>
</head>
<body>

  <section class="card card--front" aria-label="Frente do cartão">
    <div class="front-brand">
      <span class="brand-dot"></span>
      <span class="brand-name">Variel Advogados</span>
    </div>
    <p class="front-web">www.varieladvogados.com.br</p>
  </section>

  <section class="card card--contact" aria-label="Verso do cartão">
    <div class="contact-brand">
      <span class="brand-dot"></span>
      <span class="brand-name">Variel</span>
    </div>
    <div class="divider"></div>
    <div class="contact-details">
      <p class="person-name">Marcos Variel</p>
      <p class="address">Rua Helena Prado,<br>482, Torre 3, 7º andar<br>São Paulo / SP - CEP: 04512-090</p>
      <p class="contact-line">
        <svg class="contact-icon" viewBox="0 0 16 16" aria-hidden="true"><rect x="0" y="0" width="16" height="16" rx="3"/><path d="M5 3.5c.6 0 1.5 2 1.2 2.5l-.8.8c.6 1.4 1.6 2.4 3 3l.8-.8c.5-.3 2.5.6 2.5 1.2 0 1-1 2.3-2.2 2.3C6.3 12.5 3.5 9.7 3.5 6.5 3.5 4.8 4.3 3.5 5 3.5z" fill="#f4f4f3"/></svg>
        +55 11 3400-5120
      </p>
      <p class="contact-line">
        <svg class="contact-icon" viewBox="0 0 16 16" aria-hidden="true"><rect x="4" y="1" width="8" height="4"/><rect x="1" y="5" width="14" height="7" rx="1.5"/><rect x="4" y="10" width="8" height="5" fill="#f4f4f3" stroke="#a3111c" stroke-width="1.2"/></svg>
        +55 11 3400-5121
      </p>
      <p class="contact-line">
        <svg class="contact-icon" viewBox="0 0 16 16" aria-hidden="true"><rect x="0" y="3" width="16" height="10" rx="1"/><path d="M1 4l7 5 7-5" fill="none" stroke="#f4f4f3" stroke-width="1.3"/></svg>
        mvariel@varieladvogados.com.br
      </p>
    </div>
  </section>

</body>
</html>
```